Industrial Engineering firm needs a new wrap

We would like a wrap for a 2020 Morvane Telso Hatchback Sport Touring.
2 years ago, we got a wrap for a similar company - see example images 1, 2, 3, and 4. The theme for the previous wrap was something that would look like a racecar - it was a very successful wrap, and we loved driving it around. Use this as inspiration, but feel free to propose new ideas as well. ALL designs are open - something more quiet and sophisticated, or something flashy, like the previous design. We really REALLY liked the "racecar" look.
Now, we have a new logo and a new list of services. For logo options, see logo images 1-4. If necessary, we have all logo options in B&W and transparent options as well.
Company colors are:
1. Prussian Blue (#00283C)
2. Imperial Red (#E63946)
3. Powder Blue (#A8DADC)
4. Viridian Green (#119DA4)
5. Light Green (#8AEA92)
The original car color is white. No text on windows.
Our services:
- Industrial Engineering
- Drafting
- Training
www.tolvex.com
555-203-4418

Target Market(s)
Heavy industry clients. Brindleport Web Services. Oil and gas clients. Steel manufacturers.
Industry/Entity Type
Mechanical, industrial, civil, electrical engineering
Other font styles liked:
- Georgia, Lucida Sans
Requirements
Must have
- Our services: - Industrial Engineering - Drafting - Training www.tolvex.com 555-203-4418
Should not have
- No social media logos.

```html
<!DOCTYPE html>
<html lang="en">
<head>
<meta charset="utf-8">
<title>Tolvex Engineering – Hatchback Wrap</title>
<link rel="stylesheet" href="https://fonts.googleapis.com/css2?family=Marcellus&family=Tinos:ital,wght@0,700;1,700&display=swap">
<style>
  :root {
    --prussian: #00283c;
    --imperial: #c8283a;
    --imperial-light: #e63946;
    --body-white: #f2f2f2;
    --body-shade: #d9d9d9;
    --network: #e4e8ea;
    --canvas: #ffffff;
  }
  html, body { margin: 0; padding: 0; overflow: hidden; background: var(--canvas); }
  .canvas { display: block; width: 1200px; height: 902px; }
  .vehicle-body { fill: url(#bodyShade); }
  .network-zone { fill: url(#networkFade); }
  .service-band { fill: url(#bandRed); }
  .band-edge { fill: none; stroke: var(--prussian); stroke-width: 3; }
  .name-frame { fill: none; stroke: var(--prussian); stroke-width: 1.2; }
  .contact-line { font-family: "Tinos", Georgia, serif; font-weight: 700; font-size: 21px; fill: #111; }
  .company-name { font-family: "Marcellus", Georgia, serif; font-size: 44px; fill: var(--prussian); }
  .service-list { font-family: "Tinos", Georgia, serif; font-weight: 700; font-style: italic; font-size: 19px; fill: #fff; }
  .logo-dot { fill: var(--prussian); }
</style>
</head>
<body>
<svg class="canvas" viewBox="0 0 1200 902" xmlns="http://www.w3.org/2000/svg">
  <defs>
    <linearGradient id="bodyShade" x1="0" y1="0" x2="0" y2="1">
      <stop offset="0" stop-color="#e6e6e6"/>
      <stop offset="0.5" stop-color="var(--body-white)"/>
      <stop offset="1" stop-color="var(--body-shade)"/>
    </linearGradient>
    <radialGradient id="networkFade" cx="0.5" cy="0.5" r="0.5">
      <stop offset="0" stop-color="var(--network)"/>
      <stop offset="1" stop-color="var(--network)" stop-opacity="0"/>
    </radialGradient>
    <linearGradient id="bandRed" x1="0" y1="0" x2="1" y2="0">
      <stop offset="0" stop-color="var(--imperial)"/>
      <stop offset="0.5" stop-color="var(--imperial-light)"/>
      <stop offset="1" stop-color="var(--imperial)"/>
    </linearGradient>
  </defs>

  <!-- Driver side -->
  <g class="wrap-side driver-side">
    <path class="vehicle-body" role="img" aria-label="White hatchback, driver side body"
      d="M55 330 Q60 250 160 225 L380 170 Q470 85 620 70 L860 68 Q960 75 1060 120 L1120 150 Q1160 200 1150 330 L1140 360 Q1100 370 1080 372 A85 85 0 0 0 910 372 L345 378 A90 90 0 0 0 170 378 L70 372 Q55 360 55 330 Z"/>
    <ellipse class="network-zone" role="img" aria-label="Faint molecular network pattern" cx="330" cy="260" rx="120" ry="80"/>
    <ellipse class="network-zone" role="img" aria-label="Faint molecular network pattern" cx="950" cy="240" rx="130" ry="90"/>
    <path class="service-band" d="M377 376 Q392 345 424 337 L872 298 L885 300 Q872 340 858 372 L377 377 Z"/>
    <path class="band-edge" d="M377 376 Q392 345 424 337 L872 298"/>
    <g transform="rotate(-5 660 280)">
      <text class="contact-line" x="465" y="246">WWW.TOLVEX.COM | 555-203-4418</text>
      <rect class="name-frame" x="470" y="258" width="370" height="52"/>
      <rect class="logo-dot" x="432" y="268" width="30" height="30"/>
      <text class="company-name" x="482" y="301" textLength="346" lengthAdjust="spacingAndGlyphs">TOLVEX ENGINEERING</text>
      <text class="service-list" x="468" y="338">Industrial Engineering - Drafting - Training</text>
    </g>
  </g>

  <!-- Passenger side -->
  <g class="wrap-side passenger-side">
    <path class="vehicle-body" role="img" aria-label="White hatchback, passenger side body"
      d="M1145 785 Q1140 705 1040 680 L820 625 Q730 540 580 525 L340 523 Q240 530 140 575 L80 605 Q40 655 50 785 L60 815 Q100 825 120 827 A85 85 0 0 1 290 827 L855 833 A90 90 0 0 1 1030 833 L1130 827 Q1145 815 1145 785 Z"/>
    <ellipse class="network-zone" role="img" aria-label="Faint molecular network pattern" cx="270" cy="690" rx="130" ry="90"/>
    <ellipse class="network-zone" role="img" aria-label="Faint molecular network pattern" cx="920" cy="710" rx="130" ry="80"/>
    <path class="service-band" d="M329 725 L828 759 Q842 785 860 812 L360 808 Q345 765 329 725 Z"/>
    <path class="band-edge" d="M329 725 L828 759"/>
    <g transform="rotate(4 580 720)">
      <text class="contact-line" x="425" y="672">555-203-4418 | WWW.TOLVEX.COM</text>
      <rect class="name-frame" x="418" y="684" width="370" height="52"/>
      <rect class="logo-dot" x="380" y="694" width="30" height="30"/>
      <text class="company-name" x="430" y="727" textLength="346" lengthAdjust="spacingAndGlyphs">TOLVEX ENGINEERING</text>
      <text class="service-list" x="392" y="764">Industrial Engineering - Drafting - Training</text>
    </g>
  </g>
</svg>
</body>
</html>
```